Business Card for Marriage Commissioner

I am a marriage commissioner in the province of Alberta, meaning that I perform civil unions here. I have been trying to think of a unique design for my business card, something a bit different. A lot of "unique" designs seem to incorporate unique cuts or "some assembly required" or printed on plastic or meat. I would like my design to be a full colour card that is a typical business card size.

The information on the card should have:
Lon Varbeck
my occupation: Marriage Commissioner
my website: www.lonvarbeck.ca
my e-mail: lon@lonvarbeck.ca
my phone: 780-914-2086

I originally submitted a design to the printer that had a screen capture of a finduro search window, with my name and occupation in the text box. And underneath that, my phone number. Nothing else. They indicated they could not print this because it was a copyright violation.

One option on the design is I am a retired chemist-so a chemistry themed card would also be of interest, as long as it isn't a "Quiet Reagent" theme, as I have that on my other business cards already...

I would prefer a single sided card, but I am open to a double sided card if it is clever!

I would also prefer not to have pictures of male and female couples as in my position I will also marry same sex couples. Same thing for male/female symbols. Someone has submitted two graduated cylinders in love, which is very clever, and gets around this male/female type.

Thanks for your help and interest.

Target Market(s)

Young couples.

Industry/Entity Type

Plastic

Requirements
Nice to have
• chemistry ideas!
Should not have
• Male/female pictures, male/female symbols.
No QR codes.
No transparent designs, will go on paper stock.

```html
<!DOCTYPE html>
<html lang="en">
<head>
<meta charset="utf-8">
<title>Lon Varbeck — Marriage Commissioner business cards</title>
<link rel="stylesheet" href="https://fonts.googleapis.com/css2?family=Allura&family=Cinzel:wght@400&family=Jost:wght@400&display=swap">
<style>
  :root {
    --stage: #4a4a4c;
    --card-blue-top: #a6d3dc;
    --card-blue-bottom: #8cc2cc;
    --card-edge: #f4f6f6;
    --card-light: #ececec;
    --frame-blue: #a9d4dc;
    --ink: #1d1d1f;
    --title-light: #eef6f7;
    --title-blue: #8fc3cc;
    --rule-light: rgba(255,255,255,0.75);
    --rule-blue: #93c8d1;
    --icon-light: #f2f8f9;
    --icon-blue: #7fb7c2;
  }
  * { box-sizing: border-box; margin: 0; padding: 0; }
  html, body { width: 1200px; height: 890px; overflow: hidden; }
  body { background: var(--stage); position: relative; }

  .card {
    position: absolute;
    top: 115px;
    width: 380px;
    height: 660px;
    border: 8px solid var(--card-edge);
    box-shadow: 0 10px 30px rgba(0,0,0,0.35);
  }
  .card--front {
    left: 630px;
    background: linear-gradient(180deg, var(--card-blue-top), var(--card-blue-bottom));
  }
  .card--back {
    left: 190px;
    background: var(--card-light);
    border-color: var(--frame-blue);
  }

  .card__name {
    position: absolute;
    left: 0; right: 0;
    top: 318px;
    text-align: center;
    font-family: "Allura", cursive;
    font-size: 82px;
    line-height: 1;
    color: var(--ink);
  }
  .card__title {
    position: absolute;
    left: 0; right: 0;
    top: 404px;
    text-align: center;
    font-family: "Cinzel", serif;
    font-size: 13px;
    letter-spacing: 0.32em;
    color: var(--title-light);
  }
  .card--back .card__title { color: var(--title-blue); }

  .contact-list {
    position: absolute;
    left: 22px; right: 22px;
    top: 432px;
    list-style: none;
    border-top: 1px solid var(--rule-light);
  }
  .card--back .contact-list { border-top-color: var(--rule-blue); }
  .contact-list__item {
    display: flex;
    align-items: center;
    height: 60px;
    border-bottom: 1px solid var(--rule-light);
  }
  .card--back .contact-list__item { border-bottom-color: var(--rule-blue); }
  .contact-list__icon { width: 22px; height: 22px; flex: none; margin-right: 16px; }
  .contact-list__icon * { stroke: var(--icon-light); fill: none; stroke-width: 1.5; }
  .card--back .contact-list__icon * { stroke: var(--icon-blue); }
  .contact-list__text {
    flex: 1;
    text-align: right;
    font-family: "Jost", sans-serif;
    font-size: 22px;
    letter-spacing: 0.12em;
    color: var(--ink);
    white-space: nowrap;
  }
</style>
</head>
<body>

<section class="card card--back" aria-label="Business card, light version">
  <h1 class="card__name">Lon Varbeck</h1>
  <p class="card__title">Marriage Commissioner</p>
  <ul class="contact-list">
    <li class="contact-list__item">
      <svg class="contact-list__icon" viewBox="0 0 22 22" aria-hidden="true"><path d="M4 8 Q11 3 18 8 L16 10 L14 8 Q11 7 8 8 L6 10 Z"/><rect x="6" y="11" width="10" height="7" rx="1"/></svg>
      <span class="contact-list__text">780-914-2086</span>
    </li>
    <li class="contact-list__item">
      <svg class="contact-list__icon" viewBox="0 0 22 22" aria-hidden="true"><rect x="3" y="6" width="16" height="11"/><path d="M3 6 L11 12 L19 6"/></svg>
      <span class="contact-list__text">lon@lonvarbeck.ca</span>
    </li>
    <li class="contact-list__item">
      <svg class="contact-list__icon" viewBox="0 0 22 22" aria-hidden="true"><circle cx="11" cy="11" r="7.5"/><ellipse cx="11" cy="11" rx="3.5" ry="7.5"/><path d="M3.5 11 H18.5"/></svg>
      <span class="contact-list__text">www.lonvarbeck.ca</span>
    </li>
  </ul>
</section>

<section class="card card--front" aria-label="Business card, blue version">
  <h1 class="card__name">Lon Varbeck</h1>
  <p class="card__title">Marriage Commissioner</p>
  <ul class="contact-list">
    <li class="contact-list__item">
      <svg class="contact-list__icon" viewBox="0 0 22 22" aria-hidden="true"><path d="M4 8 Q11 3 18 8 L16 10 L14 8 Q11 7 8 8 L6 10 Z"/><rect x="6" y="11" width="10" height="7" rx="1"/></svg>
      <span class="contact-list__text">780-914-2086</span>
    </li>
    <li class="contact-list__item">
      <svg class="contact-list__icon" viewBox="0 0 22 22" aria-hidden="true"><rect x="3" y="6" width="16" height="11"/><path d="M3 6 L11 12 L19 6"/></svg>
      <span class="contact-list__text">lon@lonvarbeck.ca</span>
    </li>
    <li class="contact-list__item">
      <svg class="contact-list__icon" viewBox="0 0 22 22" aria-hidden="true"><circle cx="11" cy="11" r="7.5"/><ellipse cx="11" cy="11" rx="3.5" ry="7.5"/><path d="M3.5 11 H18.5"/></svg>
      <span class="contact-list__text">www.lonvarbeck.ca</span>
    </li>
  </ul>
</section>

</body>
</html>
```